Small butcher shop from Austria needs great powerpoint presentation

We are looking for a powerpoint template for our new CI - it should be modern and clear.

Logo (2 Versions), Slogan, Business Card and Car-Wrap-Design already exist. (See documents below.)

We won't use much text. About 50% of the presentation should be pictures, included in different ways.

We are a family business in Upper Austria, only process animals from farms in the immediate vicinity, produce the products by hand, value animal welfare and short transport routes and avoid packaging as much as possible.

The design should be modern and clear.

Font styles to use
Sans Serif

Requirements
Should not have
• Use the red color sparingly. Only use sans serif fonts (Myriad Pro - if possible). The logo needs to be on first and last page only.

```html
<!DOCTYPE html>
<html lang="en">
<head>
<meta charset="utf-8">
<title>Haldner – Presentation Template</title>
<link href="https://fonts.googleapis.com/css2?family=Roboto+Condensed:wght@400;700&family=Roboto:wght@400&display=swap" rel="stylesheet">
<style>
:root{
  --page:#e4e5e7;
  --slide:#eceeef;
  --wine:#7b0f1f;
  --wine-dark:#650b18;
  --grey:#6c6c6c;
  --ornament:#c4c2bf;
  --text:#2c2c2c;
  --white:#ffffff;
}
*{margin:0;padding:0;box-sizing:border-box}
html,body{width:1200px;height:3886px;overflow:hidden;background:var(--page)}
body{position:relative;font-family:"Roboto",Arial,sans-serif;color:var(--text)}
.slide{position:absolute;left:94px;width:985px;height:555px;overflow:hidden;background:var(--slide);box-shadow:0 2px 6px rgba(0,0,0,.18)}
.scenery{position:absolute;inset:0;background:linear-gradient(180deg,#e9ecee 0%,#eef0ef 45%,#e7eae8 70%,#eceeee 100%)}
.scenery::after{content:"";position:absolute;right:0;top:0;width:45%;height:100%;background:linear-gradient(90deg,rgba(225,222,216,0) 0%,rgba(214,210,203,.55) 100%)}
.flourish{position:absolute;top:0;width:270px;height:170px}
.flourish.left{left:0;background:radial-gradient(ellipse at 25% 35%,rgba(190,188,184,.75) 0%,rgba(200,198,194,.35) 45%,rgba(236,238,239,0) 72%)}
.flourish.right{right:0;background:radial-gradient(ellipse at 75% 35%,rgba(190,188,184,.75) 0%,rgba(200,198,194,.35) 45%,rgba(236,238,239,0) 72%)}
.brand-mark{position:absolute;left:50%;transform:translateX(-50%);text-align:center;color:var(--wine);font-family:"Roboto Condensed",Arial,sans-serif;font-weight:700;line-height:1}
.brand-mark .dot{display:block;margin:0 auto;border-radius:50%;background:var(--grey)}
.brand-mark.large{top:110px;font-size:124px;letter-spacing:8px}
.brand-mark.large .dot{width:46px;height:46px;margin-bottom:30px}
.brand-mark.small{top:24px;font-size:34px;letter-spacing:2px}
.brand-mark.small .dot{width:16px;height:16px;margin-bottom:8px}
.ribbon{position:absolute;left:0;right:0;top:448px;height:46px;background:var(--wine)}
.name-plate{position:absolute;left:299px;top:425px;width:386px;height:94px;background:var(--slide);border:2px solid var(--wine);outline:1px solid var(--wine);outline-offset:3px;text-align:center;font-family:"Roboto Condensed",Arial,sans-serif;color:var(--wine);font-size:25px;line-height:31px;padding-top:14px}
.slide-title{position:absolute;font-family:"Roboto Condensed",Arial,sans-serif;font-weight:700;color:var(--wine);font-size:25px;line-height:31px;text-align:center}
.body-copy{position:absolute;font-size:10.5px;line-height:18px;text-align:justify;text-align-last:center;color:var(--text)}
.body-copy p+p{margin-top:18px}
.footer{position:absolute;left:0;right:0;bottom:0;height:47px;background:var(--wine);font-size:10px;color:var(--white)}
.footer .notch{position:absolute;left:468px;top:-22px;width:50px;height:24px}
.footer .follow{position:absolute;left:90px;top:17px;display:flex;align-items:center;gap:6px}
.footer .follow i{display:inline-block;width:18px;height:18px;border-radius:2px;background:rgba(255,255,255,.35)}
.footer .follow span{margin-right:6px}
.footer .rights{position:absolute;right:114px;top:18px}
.footer .page-no{position:absolute;right:0;top:0;width:102px;height:47px;background:var(--grey);text-align:center;line-height:47px}
.photo{position:absolute}
.photo-frame{position:absolute;left:91px;top:116px;width:395px;height:334px;border:1.5px solid var(--wine)}
.photo.cattle{left:112px;top:136px;width:354px;height:332px;background:linear-gradient(180deg,#c9b58a 0%,#6e7448 35%,#8b5a33 60%,#4b5a2b 100%);border:1.5px solid var(--wine)}
.photo.van{left:438px;top:192px;width:499px;height:215px;border-radius:60px 24px 30px 30px;background:linear-gradient(160deg,#4c5563 0%,#3a4250 55%,#2a2f37 100%)}
.closing{background:var(--wine)}
.closing .scenery{background:linear-gradient(180deg,#7d1323 0%,#76101f 55%,#6e0e1c 100%)}
.closing .scenery::after{background:linear-gradient(90deg,rgba(110,14,28,0) 0%,rgba(90,10,22,.5) 100%)}
.closing .brand-mark{color:var(--white)}
.closing .brand-mark.large{top:24px}
.closing .brand-mark .dot{background:var(--white)}
.closing .name-plate{top:356px;background:transparent;border-color:var(--white);outline-color:var(--white);color:var(--white)}
.contact-row{position:absolute;left:0;right:0;top:487px;height:40px;color:var(--white);font-family:"Roboto Condensed",Arial,sans-serif;font-size:15px;line-height:19px}
.contact-item{position:absolute;top:0;display:flex;gap:12px;align-items:center}
.contact-item svg{width:16px;height:16px;flex:none}
.contact-divider{position:absolute;top:2px;width:1px;height:36px;background:rgba(255,255,255,.55)}
</style>
</head>
<body>

<section class="slide" style="top:80px">
  <div class="scenery" role="img" aria-label="Faded photo of an alpine lakeside village with mountains"></div>
  <div class="flourish left" role="img" aria-label="Grey baroque scroll ornament"></div>
  <div class="flourish right" role="img" aria-label="Grey baroque scroll ornament"></div>
  <div class="brand-mark large"><span class="dot"></span>HALDNER</div>
  <div class="ribbon"></div>
  <div class="name-plate">Franz Haldner<br>Master butcher &amp; meat sommelier</div>
</section>

<section class="slide" style="top:712px">
  <div class="scenery" role="img" aria-label="Faded photo of an alpine lakeside village with mountains"></div>
  <div class="flourish left" role="img" aria-label="Grey baroque scroll ornament"></div>
  <div class="flourish right" style="top:auto;bottom:47px;height:130px" role="img" aria-label="Grey baroque scroll ornament"></div>
  <div class="brand-mark small"><span class="dot"></span>HALDNER</div>
  <div class="photo-frame"></div>
  <div class="photo cattle" role="img" aria-label="Photo of brown and white cattle in a meadow at sunset"></div>
  <h2 class="slide-title" style="left:533px;width:336px;top:133px">Nemo enim ipsam voluptatem<br>quia voluptas si</h2>
  <div class="body-copy" style="left:533px;width:336px;top:190px">
    <p>Lorem ipsum dolor sit amet, consectetur adipiscing elit, sed do eiusmod tempor incididunt ut labore et dolore magna aliqua. Ut enim ad minim veniam, quis nostrud exercitation ullamco laboris nisi ut aliquip ex ea commodo consequat. Duis aute irure dolor in reprehenderit in voluptate velit esse cillum dolore eu fugiat nulla pariatur. Excepteur sint occaecat cupidatat non proident, sunt in culpa qui officia deserunt mollit anim id est laborum.</p>
    <p>Lorem ipsum dolor sit amet, consectetur adipiscing elit, sed do eiusmod tempor incididunt ut labore et dolore magna aliqua. Ut enim ad minim veniam, quis nostrud exercitation ullamco laboris nisi ut aliquip ex ea commodo consequat. Duis aute irure dolor in reprehenderit in voluptate velit esse cillum dolore eu fugiat nulla pariatur. Excepteur sint occaecat cupidatat non proident, sunt in culpa qui officia deserunt mollit anim id est laborum.</p>
  </div>
  <footer class="footer">
    <svg class="notch" viewBox="0 0 50 24"><path d="M0 24 Q18 22 25 2 Q32 22 50 24Z" fill="var(--wine)"/></svg>
    <div class="follow"><span>Follow us :</span><i></i><i></i><i></i></div>
    <div class="rights">© 2022 Company name. All Rights Reserved.</div>
    <div class="page-no">PAGE NO : 02</div>
  </footer>
</section>

<section class="slide" style="top:1345px">
  <div class="scenery" role="img" aria-label="Faded photo of an alpine lakeside village with mountains"></div>
  <div class="flourish left" role="img" aria-label="Grey baroque scroll ornament"></div>
  <div class="flourish right" role="img" aria-label="Grey baroque scroll ornament"></div>
  <div class="brand-mark small"><span class="dot"></span>HALDNER</div>
  <svg class="diamond-gallery" style="position:absolute;left:0;top:0" width="985" height="555" viewBox="0 0 985 555">
    <defs>
      <linearGradient id="gHang" x1="0" y1="0" x2="1" y2="1"><stop offset="0" stop-color="#d9c3bd"/><stop offset="1" stop-color="#b86a6a"/></linearGradient>
      <linearGradient id="gCut" x1="0" y1="0" x2="1" y2="1"><stop offset="0" stop-color="#e8e6e4"/><stop offset=".6" stop-color="#9c3a3a"/><stop offset="1" stop-color="#2a2a2a"/></linearGradient>
      <linearGradient id="gSteak" x1="0" y1="0" x2="1" y2="1"><stop offset="0" stop-color="#6a6a66"/><stop offset=".5" stop-color="#7e2a2a"/><stop offset="1" stop-color="#3a2a24"/></linearGradient>
      <linearGradient id="gCounter" x1="0" y1="0" x2="1" y2="1"><stop offset="0" stop-color="#9e4040"/><stop offset=".5" stop-color="#d9d6d2"/><stop offset="1" stop-color="#4a4f5c"/></linearGradient>
      <linearGradient id="gVan" x1="0" y1="0" x2="1" y2="1"><stop offset="0" stop-color="#6b7a68"/><stop offset=".55" stop-color="#3e4858"/><stop offset="1" stop-color="#2c3038"/></linearGradient>
    </defs>
    <polygon role="img" aria-label="Photo of carcasses hanging in a cold room" points="195,224 328,357 195,490 62,357" fill="url(#gHang)" stroke="#fff" stroke-width="3"/>
    <polygon role="img" aria-label="Photo of a gloved hand cutting raw beef" points="344,81 477,214 344,347 211,214" fill="url(#gCut)" stroke="#fff" stroke-width="3"/>
    <polygon role="img" aria-label="Photo of a hand holding a raw steak" points="492,224 625,357 492,490 359,357" fill="url(#gSteak)" stroke="#fff" stroke-width="3"/>
    <polygon role="img" aria-label="Photo of a butcher shop counter with meat" points="643,77 776,210 643,343 510,210" fill="url(#gCounter)" stroke="#fff" stroke-width="3"/>
    <polygon role="img" aria-label="Photo of the wrapped delivery van" points="791,224 924,357 791,490 658,357" fill="url(#gVan)" stroke="#fff" stroke-width="3"/>
  </svg>
  <footer class="footer">
    <svg class="notch" viewBox="0 0 50 24"><path d="M0 24 Q18 22 25 2 Q32 22 50 24Z" fill="var(--wine)"/></svg>
    <div class="follow"><span>Follow us :</span><i></i><i></i><i></i></div>
    <div class="rights">© 2022 Company name. All Rights Reserved.</div>
    <div class="page-no">PAGE NO : 03</div>
  </footer>
</section>

<section class="slide" style="top:1977px">
  <div class="scenery" role="img" aria-label="Faded photo of an alpine lakeside village with mountains"></div>
  <div class="flourish left" role="img" aria-label="Grey baroque scroll ornament"></div>
  <div class="flourish right" role="img" aria-label="Grey baroque scroll ornament"></div>
  <div class="brand-mark small"><span class="dot"></span>HALDNER</div>
  <h2 class="slide-title" style="left:300px;width:385px;top:108px">Nemo enim ipsam voluptatem<br>quia voluptas si</h2>
  <div class="body-copy" style="left:77px;width:336px;top:196px">
    <p>Lorem ipsum dolor sit amet, consectetur adipiscing elit, sed do eiusmod tempor incididunt ut labore et dolore magna aliqua. Ut enim ad minim veniam, quis nostrud exercitation ullamco laboris nisi ut aliquip ex ea commodo consequat. Duis aute irure dolor in reprehenderit in voluptate velit esse cillum dolore eu fugiat nulla pariatur. Excepteur sint occaecat cupidatat non proident, sunt in culpa qui officia deserunt mollit anim id est laborum.</p>
    <p>Lorem ipsum dolor sit amet, consectetur adipiscing elit, sed do eiusmod tempor incididunt ut labore et dolore magna aliqua. Ut enim ad minim veniam, quis nostrud exercitation ullamco laboris nisi ut aliquip ex ea commodo consequat. Duis aute irure dolor in reprehenderit in voluptate velit esse cillum dolore eu fugiat nulla pariatur.</p>
  </div>
  <div class="photo van" role="img" aria-label="Photo of the grey-blue delivery van with beef cut chart wrap"></div>
  <footer class="footer">
    <svg class="notch" viewBox="0 0 50 24"><path d="M0 24 Q18 22 25 2 Q32 22 50 24Z" fill="var(--wine)"/></svg>
    <div class="follow"><span>Follow us :</span><i></i><i></i><i></i></div>
    <div class="rights">© 2022 Company name. All Rights Reserved.</div>
    <div class="page-no">PAGE NO : 04</div>
  </footer>
</section>

<section class="slide" style="top:2608px">
  <div class="scenery" role="img" aria-label="Faded photo of an alpine lakeside village with mountains"></div>
  <div class="flourish left" role="img" aria-label="Grey baroque scroll ornament"></div>
  <div class="flourish right" role="img" aria-label="Grey baroque scroll ornament"></div>
  <div class="brand-mark small"><span class="dot"></span>HALDNER</div>
  <h2 class="slide-title" style="left:300px;width:385px;top:118px">Nemo enim ipsam voluptatem<br>quia voluptas si</h2>
  <svg class="hex-gallery" style="position:absolute;left:0;top:0" width="985" height="555" viewBox="0 0 985 555">
    <defs>
      <linearGradient id="hVanA" x1="0" y1="0" x2="0" y2="1"><stop offset="0" stop-color="#7a6a5a"/><stop offset=".5" stop-color="#4a5466"/><stop offset="1" stop-color="#5a6a48"/></linearGradient>
      <linearGradient id="hMeat" x1="0" y1="0" x2="1" y2="1"><stop offset="0" stop-color="#b36a66"/><stop offset=".5" stop-color="#8e2f30"/><stop offset="1" stop-color="#5a3a34"/></linearGradient>
      <linearGradient id="hVanB" x1="0" y1="0" x2="0" y2="1"><stop offset="0" stop-color="#9fb3c8"/><stop offset=".5" stop-color="#3f4a5c"/><stop offset="1" stop-color="#5d6b4a"/></linearGradient>
    </defs>
    <polygon role="img" aria-label="Photo of the delivery van parked by an old barn" points="220,210 335,272 335,398 220,460 106,398 106,272" fill="url(#hVanA)"/>
    <polygon role="img" aria-label="Photo of meat hanging in a cold room" points="495,210 610,272 610,398 495,460 380,398 380,272" fill="url(#hMeat)"/>
    <polygon role="img" aria-label="Photo of the delivery van from the side" points="768,210 883,272 883,398 768,460 653,398 653,272" fill="url(#hVanB)"/>
    <g fill="var(--wine)">
      <polygon points="359,195 383,207 383,231 359,243 335,231 335,207"/>
      <polygon points="632,195 656,207 656,231 632,243 608,231 608,207"/>
      <polygon points="359,420 383,432 383,456 359,468 335,456 335,432"/>
      <polygon points="632,420 656,432 656,456 632,468 608,456 608,432"/>
    </g>
  </svg>
  <footer class="footer">
    <svg class="notch" viewBox="0 0 50 24"><path d="M0 24 Q18 22 25 2 Q32 22 50 24Z" fill="var(--wine)"/></svg>
    <div class="follow"><span>Follow us :</span><i></i><i></i><i></i></div>
    <div class="rights">© 2022 Company name. All Rights Reserved.</div>
    <div class="page-no">PAGE NO : 05</div>
  </footer>
</section>

<section class="slide closing" style="top:3241px">
  <div class="scenery" role="img" aria-label="Photo of an alpine lakeside village toned in deep red"></div>
  <div class="brand-mark large"><span class="dot"></span>HALDNER</div>
  <div class="name-plate">Franz Haldner<br>Master butcher &amp; meat sommelier</div>
  <div class="contact-row">
    <div class="contact-item" style="left:125px">
      <svg viewBox="0 0 16 16"><path d="M8 1a5 5 0 0 0-5 5c0 4 5 9 5 9s5-5 5-9a5 5 0 0 0-5-5zm0 7a2 2 0 1 1 0-4 2 2 0 0 1 0 4z" fill="#fff"/></svg>
      <span>Lindenweg 7 |<br>4850 Talbach</span>
    </div>
    <div class="contact-divider" style="left:288px"></div>
    <div class="contact-item" style="left:321px">
      <svg viewBox="0 0 16 16"><rect x="1" y="3" width="14" height="10" rx="1" fill="#fff"/><path d="M1.5 4 8 9l6.5-5" stroke="var(--wine)" stroke-width="1.3" fill="none"/></svg>
      <span>Email :<br>metzgerei@haldner.at</span>
    </div>
    <div class="contact-divider" style="left:500px"></div>
    <div class="contact-item" style="left:528px">
      <svg viewBox="0 0 16 16"><circle cx="8" cy="8" r="7" fill="#fff"/><path d="M1 8h14M8 1c-3 3-3 11 0 14M8 1c3 3 3 11 0 14" stroke="var(--wine)" stroke-width="1" fill="none"/></svg>
      <span>Website:<br>www.haldner.at</span>
    </div>
    <div class="contact-divider" style="left:679px"></div>
    <div class="contact-item" style="left:706px">
      <svg viewBox="0 0 16 16"><path d="M4 1l3 3-2 2c1 2 3 4 5 5l2-2 3 3-2 3C7 15 1 9 1 3z" fill="#fff"/></svg>
      <span>Phone :<br>+43 660 123 45 67</span>
    </div>
  </div>
</section>

</body>
</html>
```